Vemtra Group: Business Card for a high end technology company

We need a cool new design for our business cards using our cloud logo. We are a technology consulting business. We pride ourselves on be the best of the best. We mainly focus on cloud solutions and managed services. We need a business card that sets us apart from the other technology companies in the area and allows us to stand out.

Target Market(s)

Technology departments, CIO, CEOs, and Information Technology Staff.

Industry/Entity Type

Information Technology

Contact Information for Business Card

Must have the logo and our name.
Must have employee name, email address, office phone, cell phone and website.
Need to have all info on one side a cool design on backside.

Font styles to use
Serif
Sans Serif

Requirements
Must have
• Must have the logo and our name.
• Must have employee name, email address, office phone, cell phone and website.
• Need to have all info on one side a cool design on back side.
• Must be a crisp clean design, not too busy or confusing.

```html
<!DOCTYPE html>
<html lang="en">
<head>
<meta charset="utf-8">
<title>Vemtra Group Business Card</title>
<link rel="stylesheet" href="https://fonts.googleapis.com/css2?family=Open+Sans:wght@400;600;700&family=Questrial&display=swap">
<style>
  :root {
    --bg: #e9ebee;
    --card: #ffffff;
    --ink: #333333;
    --ink-soft: #555555;
    --brand: #1e88d9;
    --brand-light: #2fb4f2;
    --brand-deep: #2272c0;
    --rule: #c9ccd0;
  }
  * { margin: 0; padding: 0; box-sizing: border-box; }
  html, body {
    width: 1105px;
    height: 1200px;
    overflow: hidden;
    background: var(--bg);
    font-family: "Open Sans", Arial, sans-serif;
  }
  .canvas { position: relative; width: 1105px; height: 1200px; }
  .card {
    position: absolute;
    left: 192px;
    width: 720px;
    height: 412px;
    border-radius: 22px;
    overflow: hidden;
  }
  /* Front */
  .card-front { top: 166px; background: var(--card); }
  .brand-block {
    position: absolute;
    left: 30px;
    width: 330px;
    top: 180px;
    text-align: center;
  }
  .brand-name {
    display: inline-flex;
    align-items: center;
    gap: 12px;
    font-family: "Questrial", Arial, sans-serif;
    font-size: 38px;
    color: var(--ink);
    line-height: 1;
  }
  .brand-dot {
    width: 24px; height: 24px;
    border-radius: 50%;
    background: var(--brand);
  }
  .brand-url {
    margin-top: 10px;
    font-size: 12px;
    font-weight: 700;
    color: var(--ink);
  }
  .divider {
    position: absolute;
    left: 359px; top: 103px;
    width: 1px; height: 187px;
    background: var(--rule);
  }
  .person { position: absolute; left: 390px; top: 106px; }
  .person-name { font-size: 25px; font-weight: 600; color: var(--brand); line-height: 32px; }
  .person-title { font-size: 17px; color: var(--ink); line-height: 24px; }
  .contact-list { list-style: none; margin-top: 15px; }
  .contact-item {
    display: flex; align-items: center; gap: 12px;
    font-size: 17px; color: var(--ink-soft); line-height: 27.5px;
  }
  .contact-icon { width: 16px; height: 16px; fill: var(--brand); flex: none; }
  .band-rule {
    position: absolute; left: 0; right: 0; top: 374px;
    height: 3px; background: #4a5560;
  }
  .band {
    position: absolute; left: 0; right: 0; top: 379px; bottom: 0;
    background: linear-gradient(90deg, var(--brand-deep), var(--brand-light) 50%, var(--brand-deep));
  }
  /* Back */
  .card-back {
    top: 622px;
    background: radial-gradient(ellipse at 50% 45%, var(--brand-light) 0%, #249ae0 45%, var(--brand-deep) 100%);
    color: #ffffff;
    text-align: center;
  }
  .back-brand {
    position: absolute; left: 0; right: 0; top: 150px;
    display: flex; justify-content: center; align-items: center; gap: 16px;
    font-family: "Questrial", Arial, sans-serif;
    font-size: 58px; line-height: 1;
  }
  .back-dot { width: 36px; height: 36px; border-radius: 50%; background: #ffffff; }
  .back-url {
    position: absolute; left: 0; right: 0; top: 286px;
    font-size: 20px; font-weight: 700; letter-spacing: 0.5px;
  }
</style>
</head>
<body>
<main class="canvas">
  <section class="card card-front" aria-label="Business card front">
    <div class="brand-block">
      <div class="brand-name"><span class="brand-dot"></span>Vemtra Group</div>
      <div class="brand-url">www.vemtragroup.com</div>
    </div>
    <div class="divider"></div>
    <div class="person">
      <div class="person-name">Daniel Reyes</div>
      <div class="person-title">CEO/Founder</div>
      <ul class="contact-list">
        <li class="contact-item">
          <svg class="contact-icon" viewBox="0 0 16 16"><path d="M3.2 1l2.6 3-1.3 2a8 8 0 0 0 5.5 5.5l2-1.3 3 2.6-1.6 2.2C8 15.5.5 8 .9 2.6z"/></svg>
          555 210 4417
        </li>
        <li class="contact-item">
          <svg class="contact-icon" viewBox="0 0 16 16"><path d="M4 0h8a1.5 1.5 0 0 1 1.5 1.5v13A1.5 1.5 0 0 1 12 16H4a1.5 1.5 0 0 1-1.5-1.5v-13A1.5 1.5 0 0 1 4 0zm0.5 2v10h7V2zM8 12.8a1 1 0 1 0 0 2 1 1 0 0 0 0-2z"/></svg>
          555 318 6620
        </li>
        <li class="contact-item">
          <svg class="contact-icon" viewBox="0 0 16 16"><path d="M1 3h14v10H1zm1.5 1.4V12h11V4.4L8 8.8z M2.8 4L8 7.8 13.2 4z"/></svg>
          hello@vemtra.net
        </li>
        <li class="contact-item">
          <svg class="contact-icon" viewBox="0 0 16 16"><circle cx="8" cy="8" r="7.5"/><path d="M8 .5v15M.5 8h15M3 3.5c3 2 7 2 10 0M3 12.5c3-2 7-2 10 0" stroke="#fff" stroke-width="1" fill="none"/></svg>
          www.vemtra.net
        </li>
      </ul>
    </div>
    <div class="band-rule"></div>
    <div class="band"></div>
  </section>

  <section class="card card-back" aria-label="Business card back">
    <div class="back-brand"><span class="back-dot"></span>Vemtra Group</div>
    <div class="back-url">www.vemtragroup.com</div>
  </section>
</main>
</body>
</html>
```